Business Card Design - Halden Joinery Ltd.

Design a business card, including a new logo for a new company in Vancouver, British Columbia, Canada.

The logo must be available as a separate file.

The card should include all company information including:
Halden Joinery Ltd.
2786 Larchmoor Crescent
Millbrook, B.C. V7K 2P9
Telehone: 604-XXX-XXXX
Fax: 604-XXX-XXXX
www.haldenjoinery.example

As well as individual contact information for employees:
Name
Position
Telephone
Email

The card must include a thoughtful message as well

Target Market(s)

Custom Cabinets

Industry/Entity Type

Business

Contact Information for Business Card

Important information on the front, thoughtful message on the back

Colors
fbed22
9bcb3c
0355a3
ec1f27

Requirements
Must have
• See project description
Nice to have
• images that showcase custom cabinets (european, modern and traditional) styles

```html
<!DOCTYPE html>
<html lang="en">
<head>
<meta charset="utf-8">
<title>Halden Joinery Ltd. – Business Card</title>
<link href="https://fonts.googleapis.com/css2?family=Open+Sans:wght@400;600;800&display=swap" rel="stylesheet">
<style>
  :root {
    --page-bg: #d9d9db;
    --wood-light: #b5562c;
    --wood-mid: #9a4220;
    --wood-dark: #7a3016;
    --ink: #1e1a18;
    --card-shadow: rgba(0, 0, 0, 0.35);
  }
  html, body {
    margin: 0;
    padding: 0;
    width: 1200px;
    height: 863px;
    overflow: hidden;
    background: var(--page-bg);
    font-family: "Open Sans", Arial, sans-serif;
    color: var(--ink);
  }
  .canvas {
    position: relative;
    width: 1200px;
    height: 863px;
  }
  .card {
    position: absolute;
    width: 600px;
    height: 343px;
    border-radius: 24px;
    overflow: hidden;
    box-shadow: 0 10px 24px var(--card-shadow);
  }
  .card--front { left: 110px; top: 70px; }
  .card--back  { left: 490px; top: 450px; }
  .wood-surface {
    position: absolute;
    inset: 0;
    background:
      linear-gradient(100deg, rgba(255,255,255,0.10) 0%, rgba(255,255,255,0) 35%),
      linear-gradient(180deg, var(--wood-light) 0%, var(--wood-mid) 55%, var(--wood-dark) 100%);
  }
  .contact-block {
    position: absolute;
    left: 34px;
    top: 30px;
  }
  .person-name {
    margin: 0;
    font-size: 22px;
    font-weight: 600;
    line-height: 1.1;
  }
  .person-title {
    margin: 2px 0 26px;
    font-size: 11px;
    font-weight: 400;
  }
  .contact-list {
    list-style: none;
    margin: 0;
    padding: 0;
    font-size: 13px;
    line-height: 1.45;
  }
  .contact-list li {
    display: flex;
    align-items: flex-start;
    gap: 8px;
  }
  .contact-icon {
    width: 11px;
    height: 11px;
    margin-top: 4px;
    flex: none;
    fill: var(--ink);
  }
  .logo-name {
    position: absolute;
    display: flex;
    align-items: center;
    gap: 10px;
    font-weight: 800;
    color: var(--ink);
    white-space: nowrap;
  }
  .logo-name__mark {
    background: var(--ink);
    border-radius: 50%;
    flex: none;
  }
  .card--front .logo-name {
    right: 40px;
    top: 128px;
    font-size: 24px;
  }
  .card--front .logo-name__mark { width: 20px; height: 20px; }
  .card--back .logo-name {
    left: 50%;
    top: 120px;
    transform: translateX(-50%);
    font-size: 40px;
  }
  .card--back .logo-name__mark { width: 32px; height: 32px; }
  .website {
    position: absolute;
    margin: 0;
    font-size: 14px;
    font-weight: 600;
  }
  .card--front .website { right: 40px; bottom: 34px; }
  .card--back .website  { left: 150px; top: 220px; }
</style>
</head>
<body>
<main class="canvas">

  <section class="card card--front" aria-label="Business card front">
    <div class="wood-surface" role="img" aria-label="Polished reddish-brown wood grain texture"></div>

    <div class="contact-block">
      <h1 class="person-name">Name Here</h1>
      <p class="person-title">Title Here</p>
      <ul class="contact-list">
        <li>
          <svg class="contact-icon" viewBox="0 0 12 12"><rect x="3" y="0.5" width="6" height="11" rx="1.2"/></svg>
          604-XXX-XXXX
        </li>
        <li>
          <svg class="contact-icon" viewBox="0 0 12 12"><rect x="1" y="1" width="10" height="10" rx="1.5"/></svg>
          604-XXX-XXXX
        </li>
        <li>
          <svg class="contact-icon" viewBox="0 0 12 12"><rect x="3" y="0.5" width="6" height="3"/><rect x="0.5" y="4" width="11" height="5" rx="1"/><rect x="3" y="8" width="6" height="3.5"/></svg>
          604-XXX-XXXX
        </li>
        <li>
          <svg class="contact-icon" viewBox="0 0 12 12"><path d="M0.5 2.5h11v7h-11z M0.5 2.5l5.5 4 5.5-4"/></svg>
          info@haldenjoinery.example
        </li>
        <li>
          <svg class="contact-icon" viewBox="0 0 12 12"><path d="M6 0.5a4 4 0 0 1 4 4c0 3-4 7-4 7s-4-4-4-7a4 4 0 0 1 4-4z"/></svg>
          <span>2786 Larchmoor Crescent<br>Millbrook, B.C. V7K 2P9</span>
        </li>
      </ul>
    </div>

    <div class="logo-name">
      <span class="logo-name__mark"></span>
      <span>Halden Joinery</span>
    </div>

    <p class="website">www.haldenjoinery.example</p>
  </section>

  <section class="card card--back" aria-label="Business card back">
    <div class="wood-surface" role="img" aria-label="Polished reddish-brown wood grain texture"></div>

    <div class="logo-name">
      <span class="logo-name__mark"></span>
      <span>Halden Joinery</span>
    </div>

    <p class="website">www.haldenjoinery.example</p>
  </section>

</main>
</body>
</html>
```